Greyfield Ridge Medical Website to make connecting and communicating easier

To create a unique, user-friendly, professional website for patients and professionals to access education/ information, forms, appointments, contact details, and data about us, and for us to have the capacity to link to various cloud-based platforms.
To use the logo design and colour scheme we have just sourced.

WEBSITE to be eye catching, Inspiring and alluring
- efficient and logical
- professional and trustworthy appearance
- health focus "living health matters"
- user friendly
- ability to link with cloud-based software and video conferencing tools/ telehealth
- colours- black/ white teal and ?silver

PAGES:
page 1 - Our clinic and staff, services offered, contact us- address/ map / contact details- social media connections
page 2- patients and visitors - New patient forms to complete, news and patient informtion (educatinal)
page 3 - health professionals -referral forms, research and education
page 3- online appointments
page 4 - Quick links - partners, other services
page 5- privacy policy, disclaimer

HI, Could we please extend the deadline another 5 days, so sorry just struggling with my workload to be able to keep up and I am wanting to liaise more with the designer that I will choose. I am so happy with PixelHarbor and all the designers - thank you! Thank you so much!!

Target Market(s)

Patients - mostly over 60's so the website must be minimal clicks and simple to navigate
Professionals - for education and access forms

Industry/Entity Type

Health Care

Coding

Coded - Design and coding required

Number of Pages Required

5+ page

Font styles to use
Sans Serif
Script

Colors
33b8a4
86cfc6

Requirements
Must have
• WEBSITE to be eye catching, Inspiring and alluring
- efficient and logical
- user friendly

WEBSITE - professional and user friendly
- ability to link with cloud based software and videoconferencing/ telehealth
Nice to have
• clean and crisp presentation
happy for an innovative look
room to add more services and ability to link pages and resources
Should not have
• Please ensure the website is not:
clunky
difficult to navigate
common and cheap looking

```html
<!DOCTYPE html>
<html lang="en">
<head>
<meta charset="utf-8">
<title>Greyfield Ridge Medical</title>
<link href="https://fonts.googleapis.com/css2?family=Montserrat:wght@400;500;600;700&display=swap" rel="stylesheet">
<style>
:root{
  --teal:#33b8a4;
  --teal-soft:#86cfc6;
  --deep:#00656f;
  --ink:#1d1d1d;
  --muted:#555;
  --card:#f4faf9;
  --footer:#ececec;
  --white:#fff;
}
*{box-sizing:border-box;margin:0;padding:0}
html,body{width:1200px;height:3604px;overflow:hidden}
body{font-family:'Montserrat',sans-serif;color:var(--ink);background:var(--white);position:relative}
a{color:inherit;text-decoration:none}
svg{display:block}

/* top bar */
.topbar{position:absolute;left:0;top:0;width:1200px;height:32px;background:var(--white);font-size:12px}
.social{position:absolute;left:62px;top:10px;display:flex;gap:10px}
.social span{width:11px;height:11px;border-radius:50%;background:#222;display:block}
.address{position:absolute;left:476px;top:9px;display:flex;align-items:center;gap:6px;color:#333;white-space:nowrap}
.top-phone{position:absolute;left:806px;top:0;width:147px;height:32px;background:#2ec4c8;color:#fff;font-weight:600;font-size:15px;display:flex;align-items:center;justify-content:center;gap:7px}
.top-book{position:absolute;left:953px;top:0;width:173px;height:32px;background:var(--deep);color:#fff;font-weight:600;font-size:12px;display:flex;align-items:center;justify-content:center;gap:8px}

/* header */
.header{position:absolute;left:0;top:32px;width:1200px;height:87px;background:var(--deep)}
.brand{position:absolute;left:67px;top:30px;display:flex;align-items:center;gap:8px;color:#fff;font-weight:600;font-size:16px;white-space:nowrap}
.brand i{width:14px;height:14px;border:2px solid #fff;border-radius:50%;display:block}
.nav{position:absolute;left:323px;top:39px;display:flex;height:48px}
.nav a{color:#fff;font-size:13px;font-weight:600;display:flex;align-items:center;padding:0 19px;white-space:nowrap}
.nav a.active{background:var(--teal);width:90px;justify-content:center;padding:0}

/* hero */
.hero{position:absolute;left:0;top:119px;width:1200px;height:485px;background:var(--teal);color:#fff}
.hero h1{position:absolute;left:76px;top:110px;width:500px;font-size:31px;font-weight:600;letter-spacing:.3px;white-space:nowrap}
.hero .sub{position:absolute;left:76px;top:168px;font-size:18px;font-weight:600;line-height:25px}
.hero .note{position:absolute;left:76px;top:224px;font-size:12px}
.hero .phone{position:absolute;left:76px;top:264px;font-size:25px;font-weight:600;display:flex;align-items:center;gap:10px}
.btn-dark{background:var(--deep);color:#fff;font-weight:600;display:flex;align-items:center;justify-content:center;gap:9px;text-transform:uppercase}
.hero .btn-dark{position:absolute;left:76px;top:314px;width:182px;height:46px;font-size:17px}
.hero-photo{position:absolute;left:594px;top:32px;width:575px;height:369px;background:linear-gradient(100deg,#1e9fc0 0%,#3fb4d0 45%,#c9d4da 70%,#eef1f3 100%)}
.dots{position:absolute;left:558px;top:442px;display:flex;gap:18px}
.dots span{width:16px;height:16px;border:2px solid #fff;border-radius:50%;position:relative}
.dots span::after{content:"";position:absolute;left:3px;top:3px;width:6px;height:6px;border-radius:50%;background:#fff}

/* welcome */
.welcome h2{position:absolute;left:0;top:648px;width:1200px;text-align:center;font-size:31px;font-weight:600}
.welcome p{position:absolute;left:300px;top:704px;width:600px;text-align:center;font-size:13px;line-height:19px;color:#333}
.team-intro{position:absolute;left:84px;top:852px;width:270px}
.team-intro h3{font-size:19px;font-weight:600;margin-bottom:22px}
.team-intro p{font-size:13.5px;line-height:19px;color:#333}
.team-intro .btn-dark{margin-top:24px;width:177px;height:38px;font-size:13px}
.doc{position:absolute;width:175px}
.doc .photo{width:175px;height:188px;background:linear-gradient(180deg,#e6ebee,#cfd8dc)}
.doc h4{font-size:10.5px;font-weight:700;margin-top:15px;text-transform:uppercase}
.doc p{font-size:10px;color:#444;margin-top:5px;line-height:14px}

/* services */
.services{position:absolute;left:0;top:1404px;width:1200px;height:609px;background:var(--deep);color:#fff}
.services h2{position:absolute;left:0;top:38px;width:1200px;text-align:center;font-size:30px;font-weight:600}
.services .lead{position:absolute;left:330px;top:98px;width:540px;text-align:center;font-size:13.5px;line-height:19px}
.services .offer{position:absolute;left:0;top:170px;width:1200px;text-align:center;font-size:13.5px}
.svc{position:absolute;width:337px;height:94px;background:var(--card);color:var(--ink);display:flex;align-items:center}
.svc .tick{margin-left:25px;width:18px;flex:none}
.svc span{margin-left:20px;font-size:15px;font-weight:600;line-height:19px;width:190px}
.svc .go{position:absolute;right:0;top:0;width:57px;height:94px;background:var(--teal);display:flex;align-items:center;justify-content:center}

/* telehealth */
.tele{position:absolute;left:71px;top:2043px;width:1058px;height:378px;border:1px solid #ccc}
.tele h2{position:absolute;left:39px;top:26px;font-size:31px;font-weight:600}
.tele p{position:absolute;left:39px;width:370px;font-size:13px;line-height:19px;color:#333}
.tele .btn-dark{position:absolute;left:40px;top:308px;width:183px;height:46px;font-size:17px}
.tele-photo{position:absolute;left:435px;top:-1px;width:624px;height:378px;background:linear-gradient(120deg,#2c4a2a 0%,#6a7d52 35%,#bfae93 60%,#a47a55 100%)}

/* new patient */
.newpt{position:absolute;left:71px;top:2446px;width:1058px;height:155px;background:var(--deep)}
.newpt-photo{position:absolute;left:0;top:0;width:504px;height:155px;background:linear-gradient(110deg,#d9d9d9,#f4f4f4 50%,#e2c9bd)}
.newpt h2{position:absolute;left:579px;top:28px;color:#fff;font-size:26px;font-weight:600}
.btn-teal{background:var(--teal);color:#fff;font-weight:600;text-transform:uppercase;display:flex;align-items:center;justify-content:center}
.newpt .btn-teal{position:absolute;left:579px;top:87px;width:310px;height:37px;font-size:12px}

/* news */
.news-title{position:absolute;left:0;top:2655px;width:1200px;text-align:center;font-size:30px;font-weight:600}
.post{position:absolute;top:2731px;width:322px}
.post .photo{width:322px;height:234px;position:relative}
.post .tag{position:absolute;right:0;bottom:0;width:146px;height:36px;background:var(--teal);color:#fff;font-size:11px;font-weight:600;display:flex;align-items:center;justify-content:center;text-transform:uppercase}
.post h3{font-size:17px;font-weight:600;line-height:22px;margin-top:22px}
.post .btn-dark{width:123px;height:38px;font-size:13px;margin-top:21px}

/* footer */
.footer{position:absolute;left:0;top:3130px;width:1200px;height:430px;background:var(--footer)}
.fcol{position:absolute;font-size:11px;color:#333;line-height:22px}
.fcol h5{color:var(--teal);font-size:12.5px;font-weight:600;text-transform:uppercase;margin-bottom:2px;line-height:20px}
.fcol b{font-weight:600}
.fcol .btn-teal,.fcol .btn-dark{width:173px;height:33px;font-size:12px;gap:7px}
.legal{position:absolute;left:0;top:3560px;width:1200px;height:44px;background:var(--teal);color:#fff;font-size:10px}
.legal .copy{position:absolute;left:127px;top:17px}
.legal .social{left:1010px;top:17px}
.legal .social span{background:#fff}
</style>
</head>
<body>

<div class="topbar">
  <div class="social"><span></span><span></span><span></span></div>
  <div class="address">
    <svg width="12" height="15" viewBox="0 0 12 15"><path d="M6 0a6 6 0 0 0-6 6c0 4.5 6 9 6 9s6-4.5 6-9a6 6 0 0 0-6-6zm0 8.5A2.5 2.5 0 1 1 6 3.5a2.5 2.5 0 0 1 0 5z" fill="#222"/></svg>
    27 Wattle Row, Hartwell NSW 2999 Australia
  </div>
  <a class="top-phone"><svg width="15" height="15" viewBox="0 0 24 24"><path d="M22 16.9v3a2 2 0 0 1-2.2 2A19.8 19.8 0 0 1 2.1 4.2 2 2 0 0 1 4.1 2h3a2 2 0 0 1 2 1.7c.1 1 .4 1.9.7 2.8a2 2 0 0 1-.5 2.1L8 9.9a16 16 0 0 0 6 6l1.3-1.3a2 2 0 0 1 2.1-.4c.9.3 1.8.6 2.8.7a2 2 0 0 1 1.7 2z" fill="none" stroke="#fff" stroke-width="2"/></svg>02 9555 0142</a>
  <a class="top-book"><svg width="13" height="13" viewBox="0 0 14 14"><rect x="1" y="2" width="12" height="11" fill="none" stroke="#fff" stroke-width="1.6"/><path d="M1 5h12M4 0v3M10 0v3M4 8h2M8 8h2M4 10.5h2M8 10.5h2" stroke="#fff" stroke-width="1.4"/></svg>BOOK APPOINTMENT</a>
</div>

<header class="header">
  <div class="brand"><i></i>Greyfield Ridge Medical</div>
  <nav class="nav">
    <a class="active">Home</a><a>Our Clinic &amp; Staff</a><a>Services</a><a>Patients &amp; Visitors</a><a>Health Professionals</a><a>News</a><a>Contact</a>
  </nav>
</header>

<section class="hero">
  <h1>GREYFIELD RIDGE MEDICAL</h1>
  <div class="sub">Bulk Billed Telehealth Appointments<br>Now Available*</div>
  <div class="note">*Patients must hold a Valid Medicare or DVA card. Participating GPs Only.</div>
  <div class="phone"><svg width="22" height="22" viewBox="0 0 24 24"><path d="M22 16.9v3a2 2 0 0 1-2.2 2A19.8 19.8 0 0 1 2.1 4.2 2 2 0 0 1 4.1 2h3a2 2 0 0 1 2 1.7c.1 1 .4 1.9.7 2.8a2 2 0 0 1-.5 2.1L8 9.9a16 16 0 0 0 6 6l1.3-1.3a2 2 0 0 1 2.1-.4c.9.3 1.8.6 2.8.7a2 2 0 0 1 1.7 2z" fill="none" stroke="#fff" stroke-width="1.8"/></svg>02 9555 0142</div>
  <a class="btn-dark"><svg width="16" height="16" viewBox="0 0 14 14"><rect x="1" y="2" width="12" height="11" fill="none" stroke="#fff" stroke-width="1.6"/><path d="M1 5h12M4 0v3M10 0v3M4 8h2M8 8h2M4 10.5h2M8 10.5h2" stroke="#fff" stroke-width="1.4"/></svg>Book Online</a>
  <div class="hero-photo" role="img" aria-label="Doctor in blue scrubs holding a tablet in a clinic corridor"></div>
  <div class="dots"><span></span><span></span><span></span></div>
</section>

<section class="welcome">
  <h2>Welcome to Greyfield Ridge Medical</h2>
  <p>Welcome to Greyfield Ridge Medical, family friendly bulk billing GP Clinic. Conveniently located in Hartwell Health Precinct, opposite the Hartwell Children's Hospital. Our GP Clinic offers a wide variety of services to help you and your family with all your health and wellbeing needs.</p>
</section>

<div class="team-intro">
  <h3>Our Team</h3>
  <p>Meet the Greyfield Ridge Medical team of diverse doctors who specialise in all aspects of your health care.</p>
  <a class="btn-dark">Our Clinic &amp; Staff</a>
</div>

<div class="doc" style="left:445px;top:842px"><div class="photo" role="img" aria-label="Portrait of Dr Martin Hale"></div><h4>Dr Martin Hale</h4><p>MBBS, FRACGP<br>Clinical Director</p></div>
<div class="doc" style="left:657px;top:842px"><div class="photo" role="img" aria-label="Portrait of Dr Anika Rao"></div><h4>Dr Anika Rao</h4><p>FRACGP, Diplomat ABFM</p></div>
<div class="doc" style="left:870px;top:842px"><div class="photo" role="img" aria-label="Portrait of Dr Helen Marsh"></div><h4>Dr Helen Marsh</h4><p>MD, FRACGP</p></div>
<div class="doc" style="left:445px;top:1126px"><div class="photo" role="img" aria-label="Portrait of Dr Kevin Tan"></div><h4>Dr Kevin Tan</h4><p>MD, FRACGP</p></div>
<div class="doc" style="left:657px;top:1126px"><div class="photo" role="img" aria-label="Portrait of Dr Sofia Lenz"></div><h4>Dr Sofia Lenz</h4><p>MD, FRACGP</p></div>
<div class="doc" style="left:870px;top:1126px"><div class="photo" role="img" aria-label="Portrait of Dr Peter Graves"></div><h4>Dr Peter Graves</h4><p>MD, FRACGP</p></div>

<section class="services">
  <h2>Services We Offer</h2>
  <p class="lead">At Greyfield Ridge Medical, we strive to provide professional, reliable advice and treatment for the Community . We believe in providing quality health care in a safe and friendly environment.</p>
  <p class="offer">Offering a wide range of patient services:</p>
</section>

<svg width="0" height="0" style="position:absolute">
  <defs>
    <symbol id="tick" viewBox="0 0 18 14"><path d="M1.5 7.5l5 5L16.5 1.5" fill="none" stroke="#33b8a4" stroke-width="2.4"/></symbol>
    <symbol id="arrow" viewBox="0 0 18 16"><path d="M1 8h15M9.5 1.5L16 8l-6.5 6.5" fill="none" stroke="#fff" stroke-width="2"/></symbol>
  </defs>
</svg>

<div class="svc" style="left:71px;top:1628px"><svg class="tick" height="14"><use href="#tick"/></svg><span>General Practitioner Services</span><div class="go"><svg width="18" height="16"><use href="#arrow"/></svg></div></div>
<div class="svc" style="left:431px;top:1628px"><svg class="tick" height="14"><use href="#tick"/></svg><span>Allied Health</span><div class="go"><svg width="18" height="16"><use href="#arrow"/></svg></div></div>
<div class="svc" style="left:793px;top:1628px"><svg class="tick" height="14"><use href="#tick"/></svg><span style="width:140px">Women's Health Checks</span><div class="go"><svg width="18" height="16"><use href="#arrow"/></svg></div></div>
<div class="svc" style="left:71px;top:1744px"><svg class="tick" height="14"><use href="#tick"/></svg><span>Men's Health Checks</span><div class="go"><svg width="18" height="16"><use href="#arrow"/></svg></div></div>
<div class="svc" style="left:431px;top:1744px"><svg class="tick" height="14"><use href="#tick"/></svg><span style="width:140px">Children's Health Checks</span><div class="go"><svg width="18" height="16"><use href="#arrow"/></svg></div></div>
<div class="svc" style="left:793px;top:1744px"><svg class="tick" height="14"><use href="#tick"/></svg><span>Minor Operations</span><div class="go"><svg width="18" height="16"><use href="#arrow"/></svg></div></div>
<div class="svc" style="left:71px;top:1852px"><svg class="tick" height="14"><use href="#tick"/></svg><span>Chronic Disease Management Plans</span><div class="go"><svg width="18" height="16"><use href="#arrow"/></svg></div></div>
<div class="svc" style="left:431px;top:1852px"><svg class="tick" height="14"><use href="#tick"/></svg><span>Pathology</span><div class="go"><svg width="18" height="16"><use href="#arrow"/></svg></div></div>
<div class="svc" style="left:793px;top:1852px"><svg class="tick" height="14"><use href="#tick"/></svg><span>Bereavement</span><div class="go"><svg width="18" height="16"><use href="#arrow"/></svg></div></div>

<section class="tele">
  <h2>Telehealth</h2>
  <p style="top:85px">At Greyfield Ridge Medical we value your health and ask you to do the same. Do not neglect your general/ regular health needs. All our doctors are still available for consultations via phone, video conference or face to face.</p>
  <p style="top:200px">To prevent the spread of COVID-19 the Australian government has introduced Telehealth. Your doctor at Greyfield Ridge Medical will consult with you in the usual manner via a bulk billed telephone or video link.</p>
  <a class="btn-dark"><svg width="16" height="16" viewBox="0 0 14 14"><rect x="1" y="2" width="12" height="11" fill="none" stroke="#fff" stroke-width="1.6"/><path d="M1 5h12M4 0v3M10 0v3M4 8h2M8 8h2M4 10.5h2M8 10.5h2" stroke="#fff" stroke-width="1.4"/></svg>Book Online</a>
  <div class="tele-photo" role="img" aria-label="Smiling older woman using a tablet at home beside a plant"></div>
</section>

<section class="newpt">
  <div class="newpt-photo" role="img" aria-label="Hand signing a registration form with a pen"></div>
  <h2>New Patient?</h2>
  <a class="btn-teal">Download our registration forms</a>
</section>

<h2 class="news-title">Latest Clinic News</h2>
<article class="post" style="left:83px">
  <div class="photo" role="img" aria-label="Older woman on a video call with her doctor" style="background:linear-gradient(135deg,#9a9a98,#6a6560 50%,#d6d4d0)"><span class="tag">Family Health</span></div>
  <h3>Is your Heart Health at risk?</h3>
  <a class="btn-dark">Read More</a>
</article>
<article class="post" style="left:439px">
  <div class="photo" role="img" aria-label="Physiotherapist treating a patient's arm" style="background:linear-gradient(135deg,#e7a3a0,#d9707a 50%,#f2c6c2)"><span class="tag">General Health</span></div>
  <h3>Physiotherapists will virtually track their patients' recovery</h3>
  <a class="btn-dark">Read More</a>
</article>
<article class="post" style="left:796px">
  <div class="photo" role="img" aria-label="Pregnant woman in a sunlit field" style="background:linear-gradient(135deg,#f3efd5,#c9c46a 55%,#9a8f3c)"><span class="tag">Women's Health</span></div>
  <h3>Ask the doctor: Is pregnancy glow real?</h3>
  <a class="btn-dark">Read More</a>
</article>

<footer class="footer"></footer>
<div class="fcol" style="left:127px;top:3183px">
  <h5>Our Clinic &amp; Staff</h5>Overview<br>Meet our Staff<br>Employment<br>Privacy Policy<br>Disclaimer
</div>
<div class="fcol" style="left:127px;top:3352px">
  <h5>Quick Links</h5>Flu Pandemic<br>Immunisation Schedule<br>Family Care Guide<br>Health Info Portal<br>Ask a GP<br>Wellness Hub<br>and more....
</div>
<div class="fcol" style="left:324px;top:3183px">
  <h5>Services</h5>General Practice<br>Vasectomy Centre<br>Travel Health<br>Cosmetic Clinic<br>Treatment of acute illnesses<br>Disease prevention<br>Family Health<br>Immunisations<br>Sports Health<br>Women's Health<br>Shared Maternity Care<br>Aviation medicals<br>Medical Acupuncture<br>PRP Therapy<br>Botox
</div>
<div class="fcol" style="left:522px;top:3183px;width:170px">
  <h5>Health Professionals</h5>GP liaison<br>Clinical education<br>Referral templates &amp; criteria<br><span style="display:block;line-height:14px;margin-top:4px">GP Continuing Professional Development</span>
</div>
<div class="fcol" style="left:748px;top:3183px">
  <h5>Hours &amp; Fees</h5><b>Monday to Friday:</b><br>8:00am – 11:00pm<br><div style="height:6px"></div><b>Saturday &amp; Sunday:</b><br>9:00am – 5:00pm<br><div style="height:26px"></div><b>Fees &amp; Billing</b>
</div>
<div class="fcol" style="left:923px;top:3183px;line-height:15px">
  <h5>Contact Us</h5>27 Wattle Row<br>Hartwell NSW 2999, Australia<br><div style="height:10px"></div><b>We are open 7 Days</b><br>Contact Us today to arrange<br>a GP appointment on:
  <a class="btn-teal" style="margin-top:10px;font-size:15px;height:33px"><svg width="14" height="14" viewBox="0 0 24 24"><path d="M22 16.9v3a2 2 0 0 1-2.2 2A19.8 19.8 0 0 1 2.1 4.2 2 2 0 0 1 4.1 2h3a2 2 0 0 1 2 1.7c.1 1 .4 1.9.7 2.8a2 2 0 0 1-.5 2.1L8 9.9a16 16 0 0 0 6 6l1.3-1.3a2 2 0 0 1 2.1-.4c.9.3 1.8.6 2.8.7a2 2 0 0 1 1.7 2z" fill="none" stroke="#fff" stroke-width="2"/></svg>02 9555 0142</a>
  <a class="btn-dark" style="margin-top:11px"><svg width="13" height="13" viewBox="0 0 14 14"><rect x="1" y="2" width="12" height="11" fill="none" stroke="#fff" stroke-width="1.6"/><path d="M1 5h12M4 0v3M10 0v3M4 8h2M8 8h2M4 10.5h2M8 10.5h2" stroke="#fff" stroke-width="1.4"/></svg>Book Appointment</a>
</div>

<div class="legal">
  <div class="copy">© 2020 Greyfield Ridge Medical. All rights reserved.</div>
  <div class="social"><span></span><span></span><span></span></div>
</div>

</body>
</html>
```